We need visit card and a letter paper for our website. thx

We have a beauty clinic in Switzerland.
https://wolkenbachtal.ch
We need a visit card.

Requirements
Must have
• see colors on website

```html
<!DOCTYPE html>
<html lang="de">
<head>
<meta charset="utf-8">
<title>Wolkenbachtal Beauty Clinic – Visitenkarte</title>
<link rel="stylesheet" href="https://fonts.googleapis.com/css2?family=Marcellus&family=Montserrat:wght@300;400;500&display=swap">
<style>
  :root {
    --backdrop: #2b2b2b;
    --card-dark: #262626;
    --card-light: #f7f7f7;
    --ink-light: #f2f2f2;
    --ink-muted: #a8a8a8;
    --ink-dark: #1e1e1e;
    --ink-soft: #3a3a3a;
    --rule: #6c6c6c;
  }
  * { box-sizing: border-box; margin: 0; padding: 0; }
  html, body { width: 1200px; height: 985px; overflow: hidden; }
  body {
    background: var(--backdrop);
    font-family: "Montserrat", sans-serif;
    position: relative;
  }
  .card {
    position: absolute;
    left: 290px;
    width: 620px;
    height: 370px;
    box-shadow: 0 14px 30px rgba(0,0,0,.45);
  }
  .card--front { top: 95px; background: var(--card-dark); color: var(--ink-light); }
  .card--back  { top: 520px; background: var(--card-light); color: var(--ink-dark); }

  .brand { display: flex; align-items: center; gap: 14px; }
  .brand__square { width: 14px; height: 14px; border: 1.5px solid currentColor; flex: none; }
  .brand__name { font-weight: 400; letter-spacing: .5px; }

  .card--front .brand {
    position: absolute; top: 118px; left: 0; right: 0; justify-content: center;
  }
  .card--front .brand__name { font-size: 44px; }
  .card--front .tagline {
    position: absolute; top: 186px; left: 0; right: 0; text-align: center;
    font-size: 12px; letter-spacing: 7px; color: var(--ink-muted); font-weight: 300;
  }
  .card--front .site {
    position: absolute; bottom: 40px; left: 0; right: 0; text-align: center;
    font-size: 16px; letter-spacing: 1.5px; font-weight: 400;
  }
  .site strong { font-weight: 500; }

  .card--back .brand { position: absolute; top: 48px; right: 40px; color: var(--ink-dark); }
  .card--back .brand__name { font-size: 28px; }
  .card--back .tagline {
    position: absolute; top: 90px; right: 40px;
    font-size: 9px; letter-spacing: 4.5px; color: var(--ink-soft); font-weight: 400;
  }
  .person { position: absolute; top: 150px; left: 40px; }
  .person__name { font-family: "Marcellus", serif; font-size: 24px; letter-spacing: 1px; }
  .person__role { font-size: 13px; color: var(--ink-soft); margin-top: 2px; }
  .divider {
    position: absolute; top: 216px; left: 258px; right: 40px;
    border-top: 1px solid var(--rule);
  }
  .contact { position: absolute; top: 222px; left: 40px; list-style: none; }
  .contact li { display: flex; align-items: center; gap: 12px; font-size: 13px; height: 24px; color: var(--ink-soft); }
  .contact svg { width: 13px; height: 13px; fill: var(--ink-dark); flex: none; }
  .address {
    position: absolute; bottom: 34px; right: 40px; text-align: right;
    font-size: 14px; line-height: 1.5; color: var(--ink-soft);
  }
</style>
</head>
<body>
  <section class="card card--front">
    <div class="brand"><span class="brand__square"></span><span class="brand__name">Wolkenbachtal</span></div>
    <p class="tagline">BEAUTY CLINIC</p>
    <p class="site">www.<strong>wolkenbachtal</strong>.ch</p>
  </section>

  <section class="card card--back">
    <div class="brand"><span class="brand__square"></span><span class="brand__name">Wolkenbachtal</span></div>
    <p class="tagline">BEAUTY CLINIC</p>

    <div class="person">
      <h1 class="person__name">DR. LENA MARBACH</h1>
      <p class="person__role">FÄ für Plastische Chirurgie</p>
    </div>
    <div class="divider"></div>

    <ul class="contact">
      <li>
        <svg viewBox="0 0 24 24" aria-hidden="true"><path d="M6.6 10.8a15.1 15.1 0 0 0 6.6 6.6l2.2-2.2c.3-.3.7-.4 1-.2 1.1.4 2.3.6 3.6.6.6 0 1 .4 1 1V20c0 .6-.4 1-1 1C10.6 21 3 13.4 3 4c0-.6.4-1 1-1h3.5c.6 0 1 .4 1 1 0 1.3.2 2.5.6 3.6.1.3 0 .7-.2 1z"/></svg>
        555.201.3874
      </li>
      <li>
        <svg viewBox="0 0 24 24" aria-hidden="true"><path d="M2 5h20v14H2z M2 5l10 8 10-8" fill="none" stroke="#1e1e1e" stroke-width="0"/><path d="M2 6.5 12 13l10-6.5V5H2zM2 8.8V19h20V8.8l-10 6.5z"/></svg>
        l.marbach@praxisnord.com
      </li>
      <li>
        <svg viewBox="0 0 24 24" aria-hidden="true"><circle cx="12" cy="12" r="9.5" fill="none" stroke="#1e1e1e" stroke-width="2"/><path d="M2.5 12h19M12 2.5c-3 3-3 16 0 19M12 2.5c3 3 3 16 0 19" fill="none" stroke="#1e1e1e" stroke-width="1.6"/></svg>
        www.praxisnord.com
      </li>
    </ul>

    <address class="address" style="font-style:normal">
      Bergweg 14<br>
      7499 Alpenried, Schweiz
    </address>
  </section>
</body>
</html>
```